Barrister Letterhead incorporating existing logo/design

Require new letterhead template to incorporate logo and information on 'Letter 2015' word document. Currently the information on the letterhead is very busy and would like a cleaner look.
Must look good in black and white, and colour when printed.

Target Market(s)

Professional

Industry/Entity Type

Legal

Requirements
Must have
• Clean professional look.

```html
<!DOCTYPE html>
<html lang="en">
<head>
<meta charset="utf-8">
<title>Harlow Chambers Letterhead</title>
<link href="https://fonts.googleapis.com/css2?family=EB+Garamond:wght@400;500&family=Tinos&display=swap" rel="stylesheet">
<style>
  :root {
    --navy: #1b2a4a;
    --grey: #9a9a9c;
    --tagline: #8a8a8c;
    --paper: #fafafa;
    --backdrop: #e9e9ea;
    --ink: #2a2a2a;
  }
  * { margin: 0; padding: 0; box-sizing: border-box; }
  html, body {
    width: 1200px; height: 1172px; overflow: hidden;
    background: var(--backdrop);
  }
  .letterhead {
    position: absolute;
    left: 213px; top: 39px;
    width: 656px; height: 927px;
    background: var(--paper);
    transform: scale(1.18);
    transform-origin: top left;
    overflow: hidden;
  }
  .swoosh { position: absolute; left: 0; width: 656px; }
  .swoosh--top { top: 0; height: 130px; }
  .swoosh--bottom { bottom: 0; height: 80px; }
  .brand {
    position: absolute; left: 52px; top: 55px;
    display: flex; align-items: flex-start; gap: 6px;
  }
  .brand__mark {
    width: 48px; height: 48px; background: var(--navy);
  }
  .brand__name {
    font-family: "EB Garamond", serif;
    color: var(--navy);
    font-size: 27px; line-height: 26px; font-weight: 500;
    letter-spacing: 0.2px;
  }
  .brand__tagline {
    font-family: "EB Garamond", serif;
    color: var(--tagline);
    font-size: 19.5px; line-height: 22px;
    letter-spacing: 1.6px;
    margin-top: 1px;
  }
  .contact {
    position: absolute; right: 48px; top: 835px;
    font-family: "Tinos", serif;
    font-size: 8.4px; line-height: 12.6px;
    color: var(--ink);
    text-align: right;
    letter-spacing: 0.2px;
  }
  .contact__row { display: flex; justify-content: flex-end; align-items: center; gap: 4px; }
  .contact__sep { margin: 0 3px; }
  .icon { width: 7px; height: 7px; fill: var(--ink); flex: none; }
  .contact__abn { padding-right: 11px; }
</style>
</head>
<body>
  <main class="letterhead">
    <svg class="swoosh swoosh--top" viewBox="0 0 656 130" aria-hidden="true">
      <path d="M22 0 H656 V42 C520 18 300 6 22 0 Z" fill="var(--navy)"/>
      <path d="M195 11 C400 20 560 40 656 60 V118 C600 60 420 30 195 11 Z" fill="var(--grey)"/>
      <path d="M656 60 C560 40 400 20 195 11 C420 18 580 36 656 52 Z" fill="var(--paper)"/>
    </svg>

    <header class="brand">
      <div class="brand__mark"></div>
      <div>
        <div class="brand__name">HARLOW CHAMBERS</div>
        <div class="brand__tagline">Barristers and Mediators</div>
      </div>
    </header>

    <address class="contact" style="font-style: normal;">
      <div class="contact__row">LEVEL 1 48 HARLOW STREET, KINGSPORT
        <svg class="icon" viewBox="0 0 10 10"><path d="M5 0a3.5 3.5 0 0 0-3.5 3.5C1.5 6 5 10 5 10s3.5-4 3.5-6.5A3.5 3.5 0 0 0 5 0zm0 5a1.5 1.5 0 1 1 0-3 1.5 1.5 0 0 1 0 3z"/></svg>
      </div>
      <div class="contact__row" style="padding-right:11px;">P.O. BOX 218, KINGSPORT. Q. 4870</div>
      <div class="contact__row">07 4500 0123
        <svg class="icon" viewBox="0 0 10 10"><path d="M1 3c2-2 6-2 8 0v1.5H7V3.5H3v1H1z M2 5h6l1 4H1z"/></svg>
        <span class="contact__sep">|</span>07 4500 0456
        <svg class="icon" viewBox="0 0 10 10"><path d="M3 0h4v3H3z M1 3h8v4H7v3H3V7H1z"/></svg>
      </div>
      <div class="contact__row">office@harlowbar.example
        <svg class="icon" viewBox="0 0 10 10"><path d="M0 2h10v6H0z" /><path d="M0 2l5 3.5L10 2" stroke="#fafafa" fill="none"/></svg>
        <span class="contact__sep">|</span>www.harlowchambers.example
        <svg class="icon" viewBox="0 0 10 10"><circle cx="5" cy="5" r="4.5"/><path d="M0.5 5h9M5 0.5v9" stroke="#fafafa" stroke-width="0.8"/></svg>
      </div>
      <div class="contact__row contact__abn">ABN 00 111 222 333</div>
    </address>

    <svg class="swoosh swoosh--bottom" viewBox="0 0 656 80" aria-hidden="true">
      <path d="M0 9 C160 20 320 36 440 54 C300 40 150 32 0 28 Z" fill="var(--grey)"/>
      <path d="M0 33 C180 38 360 52 470 72 C400 78 340 80 340 80 H0 Z" fill="var(--navy)"/>
    </svg>
  </main>
</body>
</html>
```